BRAMLEIGH real estate family office

Hello, Our business is a real estate intermediation activity on high-end goods (amounts exceeding € 10m) for corporate and private clients. You can see our logo on the site www.bramleigh-invented.fr We would like to keep that spirit with the hexagon that represents France (transactions between Monaco and Saint Tropez, Courchevel and Paris). And the "baseline" that is "real estate family office". The corporate logo should be and can be printed by embossing (relief). We must integrate the name, first name, phone, email and website. Finally, to imbibe the spirit of business, here is a detail of the activity. "Genuine consulting firm in real estate investments, BRAMLEIGH works with its customers as a specialized player in the high-end markets, we are recognized for our ultra-confidential approach and tailor-made, as well as the quality of our network. We broadcast any information on the market and we work exclusively through a strong relationship we have developed over the years. BRAMLEIGH is active on the French Riviera (from Monaco to Saint-Tropez), the Alps (Courchevel, Méribel, Megève) and Paris (essentially market premium). Always looking for opportunities for our clients, we work on two investment areas: residential luxury real estate (properties, vineyards, mansions, land, etc.) commercial real estate (empty office buildings or yield, hotel properties, land, etc.) "

Target Market(s)

High foreign end customers. corporate and private.

Industry/Entity Type

Real Estate

Contact Information for Business Card

LOGO
baseline
Laurent Dufossé
+33(0)6.41.57.09.64
ld@bramleigh-invented.fr
www.bramleigh-invented.fr

Font styles to use
Serif

Colors
cedeed
0255a3
3277b5
85abd2
85cae6
34a7d7
0792cd
cfdeed
1b1b1b

Requirements
Must have
• see description

```html
<!DOCTYPE html>
<html lang="en">
<head>
<meta charset="utf-8">
<title>BRAMLEIGH – business cards</title>
<link rel="stylesheet" href="https://fonts.googleapis.com/css2?family=Josefin+Sans:wght@300;400&family=Arimo:wght@400;700&display=swap">
<style>
  :root {
    --backdrop: #e4e2df;
    --card-blue: #132f6e;
    --card-black: #1b1b1b;
    --brand-blue: #0255a3;
    --soft-blue: #3277b5;
    --pale-blue: #cfdeed;
    --logo-light: #d9dee8;
    --logo-grey: #8d9096;
    --divider: #6d6f73;
    --text-white: #f2f2f2;
  }
  * { margin: 0; padding: 0; box-sizing: border-box; }
  html, body {
    width: 1200px; height: 864px; overflow: hidden;
    background: var(--backdrop);
  }
  .canvas { position: relative; width: 1200px; height: 864px; }

  .card {
    position: absolute;
    width: 520px; height: 298px;
    border-radius: 4px;
    box-shadow: 0 14px 30px rgba(0,0,0,.25);
    overflow: hidden;
  }

  /* Front */
  .card--front { left: 60px; top: 150px; background: var(--card-blue); }
  .front-brand { position: absolute; left: 110px; top: 88px; }
  .wordmark {
    font-family: "Josefin Sans", sans-serif;
    font-weight: 300;
    letter-spacing: 4px;
    line-height: 1;
  }
  .front-brand .wordmark { font-size: 50px; color: var(--logo-light); }
  .baseline {
    font-family: "Josefin Sans", sans-serif;
    font-weight: 300;
    letter-spacing: 1px;
  }
  .front-brand .baseline {
    font-size: 17px; color: var(--soft-blue);
    text-align: right; margin-top: 6px;
  }
  .front-web {
    position: absolute; left: 60px; top: 210px;
    font-family: "Josefin Sans", sans-serif; font-weight: 400;
    font-size: 13px; letter-spacing: 7px; color: var(--pale-blue); opacity: .55;
  }

  /* Back */
  .card--back { left: 620px; top: 410px; background: var(--card-black); }
  .back-brand { position: absolute; left: 28px; top: 110px; }
  .back-brand .wordmark { font-size: 30px; color: var(--logo-grey); letter-spacing: 3px; }
  .back-brand .baseline { font-size: 11px; color: var(--brand-blue); text-align: right; margin-top: 5px; }
  .divider {
    position: absolute; left: 262px; top: 70px;
    width: 1px; height: 160px; background: var(--divider);
  }
  .contact {
    position: absolute; left: 282px; top: 78px;
    font-family: "Arimo", sans-serif; color: var(--text-white);
  }
  .contact__name { font-size: 20px; font-weight: 400; color: var(--brand-blue); letter-spacing: .3px; }
  .contact__role { font-size: 12px; font-weight: 700; margin-top: 2px; }
  .contact__tagline { font-size: 15px; margin-top: 14px; }
  .contact__list { list-style: none; margin-top: 6px; }
  .contact__list li {
    display: flex; align-items: center; gap: 8px;
    font-size: 14px; line-height: 21px;
  }
  .contact__list svg { width: 13px; height: 13px; fill: var(--brand-blue); flex: none; }
</style>
</head>
<body>
<main class="canvas">

  <section class="card card--front" aria-label="Card front">
    <div class="front-brand">
      <div class="wordmark">BRAMLEIGH</div>
      <div class="baseline">real estate family office</div>
    </div>
    <div class="front-web">www.bramleigh-invented.fr</div>
  </section>

  <section class="card card--back" aria-label="Card back">
    <div class="back-brand">
      <div class="wordmark">BRAMLEIGH</div>
      <div class="baseline">real estate family office</div>
    </div>
    <div class="divider"></div>
    <div class="contact">
      <div class="contact__name">Laurent Dufossé</div>
      <div class="contact__role">CEO</div>
      <div class="contact__tagline">Real estate family office</div>
      <ul class="contact__list">
        <li>
          <svg viewBox="0 0 16 16" aria-hidden="true"><path d="M3.5 1l2.5 3-1.5 2c1 2 2.5 3.5 4.5 4.5l2-1.5 3 2.5-1.5 2.5C7 14 2 9 1 2.5z"/></svg>
          +33(0)6.41.57.09.64
        </li>
        <li>
          <svg viewBox="0 0 16 16" aria-hidden="true"><path d="M1 3h14v1.2L8 9 1 4.2zM1 5.8l7 4.8 7-4.8V13H1z"/></svg>
          ld@bramleigh-invented.fr
        </li>
        <li>
          <svg viewBox="0 0 16 16" aria-hidden="true"><path d="M8 1a7 7 0 100 14A7 7 0 008 1zm-1 2.2v1.6L5.2 6.5 3.3 6A5 5 0 017 3.2zM9.5 13l.5-2.5L8.3 9 6 9.5 5 8l1.5-1.5L9 6.3l2 1.2 2 .3A5 5 0 019.5 13z"/></svg>
          www.bramleigh-invented.fr
        </li>
      </ul>
    </div>
  </section>

</main>
</body>
</html>
```